Tovendi: National Baking Mix Company Needs a Pancake And Waffle Mix Label Design

Hi, we are looking for a front label design for a new pancake and waffle mix. We currently develop and manufacture various dry mixes for crepes, pancakes, waffles, and waffle cones. We are looking to expand our product line into the "all natural" category of foods. This new pancake mix contains the highest quality ingredients including: (whole grain brown rice flour, whole grain oat flour, golden flaxseed meal, whole grain sorghum flour, organic coconut flour, organic coconut sugar, eggs, leavening, vanilla extract, salt, spices.) We are looking for a way to communicate these ingredients to the public by means of claims like one would see on a food label. Here are a few different companies that do it well.
https://oakmillers.example/product/harvest/
https://www.quietgrove.example/collections/almond-flour-baking-mixes/products/almond-flour-pancake-waffle-mix
https://fentonoven.example/product/harvest-pancake-waffle-mix/
https://tovendi.example
Our mix is a just add water only mix and consists of whole grains, is gluten free, dairy free, soy free, preservative free, contains no artificial ingredients whatsoever, NON-GMO, kosher, low in sodium, good source of fiber and iron, contains omega-3 fatty acids etc. We need a strong and attractive design that appeals to the customer on a grocery store shelf. This mix is a healthier option compared to traditional pancake/waffle mixes but still provides great taste and texture one would expect from a pancake mix. Label design should be around 4.25"x 6.75" tall ways. We want to utilize what we have to offer in the best way possible.

Target Market(s)

All Natural, Healthy, Pancake Mix. 20yr-50yr olds primariliy

Industry/Entity Type

Grocery Store

Font styles to use
Serif
Sans Serif
Decorative

Colors

Designer to choose colors to be used in the design.

Requirements
Must have
• Name of company "Tovendi", must say "Pancake & Waffle Mix", "Just add water", "gluten free", "dairy free", "whole grains". the rest is up to you!
Nice to have
• I would like to see the claims utilized and promoted in such ways that appeal to the consumer. The all natural category of food is growing and we want to take advantage of that food category.
Should not have
• Should not say "paleo" on label. This mix is within the category but cannot be labeled as such.

```html
<!DOCTYPE html>
<html lang="en">
<head>
<meta charset="utf-8">
<title>Tovendi Pancake &amp; Waffle Mix — Front Label</title>
<link rel="stylesheet" href="https://fonts.googleapis.com/css2?family=Bebas+Neue&display=swap">
<style>
  :root {
    --backdrop: #e9e6e2;
    --label-white: #ffffff;
    --cocoa: #4a2a14;
    --rust: #b3472a;
    --syrup: #c9852e;
    --syrup-deep: #8a4a17;
    --batter: #e9cfa0;
    --berry: #262838;
  }
  * { box-sizing: border-box; margin: 0; padding: 0; }
  html, body {
    width: 1200px; height: 1200px; overflow: hidden;
    background: var(--backdrop);
  }
  .canvas { position: relative; width: 1200px; height: 1200px; }
  .label {
    position: absolute; left: 220px; top: 40px;
    width: 760px; height: 1120px;
    background: var(--label-white);
    border-radius: 40px;
    overflow: hidden;
    box-shadow: 0 10px 40px rgba(0,0,0,0.12);
    font-family: "Bebas Neue", "Arial Narrow", sans-serif;
  }
  .hang-hole {
    position: absolute; left: 308px; top: 48px;
    width: 144px; height: 36px;
    border-radius: 18px;
    background: var(--backdrop);
    box-shadow: inset 0 2px 4px rgba(0,0,0,0.25);
  }
  .title-line {
    position: absolute; left: 95px;
    line-height: 1; white-space: nowrap;
  }
  .title-pancake { top: 147px; font-size: 200px; color: var(--cocoa); letter-spacing: 1px; }
  .title-waffle  { top: 313px; font-size: 200px; color: var(--rust); letter-spacing: 1px; }
  .title-mix     { top: 481px; font-size: 155px; color: var(--rust); }
  .brand-name    { top: 599px; left: 97px; font-size: 62px; color: var(--cocoa); letter-spacing: 1px; }
  .claims {
    position: absolute; left: 291px; top: 508px;
    list-style: none;
    font-size: 37px; line-height: 42px;
    color: var(--cocoa); letter-spacing: 0.5px;
  }
  .claims .divider { padding: 0 10px; }
  .hero-photo {
    position: absolute; left: 0; right: 0; top: 650px; bottom: 0;
    background:
      radial-gradient(ellipse 30% 12% at 55% 14%, var(--berry) 0%, rgba(38,40,56,0) 100%),
      linear-gradient(180deg, rgba(255,255,255,1) 0%, var(--batter) 28%, var(--syrup) 55%, var(--batter) 72%, var(--syrup-deep) 100%);
  }
</style>
</head>
<body>
  <main class="canvas">
    <section class="label">
      <div class="hang-hole"></div>
      <h1>
        <span class="title-line title-pancake">PANCAKE</span>
        <span class="title-line title-waffle">&amp; WAFFLE</span>
        <span class="title-line title-mix">MIX</span>
      </h1>
      <ul class="claims">
        <li>Just add water<span class="divider">|</span>Gluten free</li>
        <li>Dairy free<span class="divider">|</span>Whole grains</li>
        <li>Healthy and tasty</li>
      </ul>
      <p class="title-line brand-name">TOVENDI</p>
      <div class="hero-photo" role="img" aria-label="Photo of a stack of golden pancakes drizzled with maple syrup and topped with blueberries"></div>
    </section>
  </main>
</body>
</html>
```